Brook & Thistle Labels*

Hello :) I am needing labels for my herbal tea/petal product. I am a small producer for the local restaurants (edible flowers/micro herbs & dried product). I am hoping to sell the dried product online. It will be sold in batches as it is ready so quite small/boutique and the label needs to be somewhat generic for the range of produce I make.
Feels: no/minimal plastic, product is in a reusable mason jar, we use organic/regenerative principles from soil health to end product. Treading gently on the land. High quality i.e only fresh hand picked leaf tips for the tea.

```html
<!DOCTYPE html>
<html lang="en">
<head>
<meta charset="utf-8">
<title>Brook &amp; Thistle Label</title>
<link rel="stylesheet" href="https://fonts.googleapis.com/css2?family=Barlow+Condensed:wght@400;500&family=Nunito:wght@700&family=Playfair+Display:wght@700&display=swap">
<style>
  :root {
    --ink: #2e2a2b;
    --forest: #2e4f3a;
    --moss: #4e6d3e;
    --leaf: #5e993a;
    --lime: #a9c44d;
    --label-green: #abc34f;
    --rule: #5b8f36;
    --paper: #ffffff;
    --frame: #d9d9d9;
  }
  * { box-sizing: border-box; margin: 0; padding: 0; }
  html, body { width: 1017px; height: 1200px; overflow: hidden; background: var(--paper); }
  .sheet {
    position: relative; width: 1017px; height: 1200px;
    border: 1px solid var(--frame); background: var(--paper);
    font-family: "Barlow Condensed", "Arial Narrow", sans-serif;
  }

  /* Left: jar wrap label, three panels stacked */
  .wrap { position: absolute; left: 116px; top: 43px; width: 289px; }
  .panel-info {
    position: relative; height: 290px; background: var(--paper);
    border: 1px solid #eeeeee; border-bottom: none;
  }
  .info-table {
    position: absolute; left: 17px; top: 17px; width: 254px; height: 255px;
    border: 2px solid var(--rule); transform: rotate(180deg);
    display: grid; grid-template-columns: 89px 1fr;
    grid-template-rows: 48px 70px 44px 45px 1fr;
    color: var(--ink); font-size: 11px; line-height: 1.35;
  }
  .info-table .cell { border-bottom: 2px solid var(--rule); padding: 6px 10px; }
  .info-table .cell:nth-last-child(1) { border-bottom: none; }
  .info-table .key { border-right: 2px solid var(--rule); }
  .info-table .full { grid-column: 1 / 3; }
  .info-table .origin { text-align: center; padding-top: 8px; font-size: 12px; }
  .info-table .address { padding-top: 8px; }

  .panel-brand {
    position: relative; height: 288px; background: var(--label-green);
  }
  .brand-disc {
    position: absolute; left: 70px; top: 84px; width: 134px; height: 134px;
    border-radius: 50%; background: var(--paper);
    display: flex; align-items: center; justify-content: center;
    font-family: "Nunito", sans-serif; font-weight: 700; font-size: 24px;
    color: var(--label-green); letter-spacing: -0.3px;
  }

  .panel-front {
    position: relative; height: 520px; overflow: hidden;
    background: var(--paper);
  }
  .front-art {
    position: absolute; inset: 0;
    background:
      radial-gradient(ellipse 110px 80px at 230px 40px, rgba(110,160,50,.75), transparent 70%),
      radial-gradient(ellipse 120px 90px at 80px 90px, rgba(170,200,90,.55), transparent 70%),
      radial-gradient(ellipse 150px 70px at 150px 420px, rgba(190,210,100,.5), transparent 70%),
      radial-gradient(ellipse 170px 90px at 200px 500px, rgba(120,170,60,.6), transparent 70%),
      radial-gradient(ellipse 70px 140px at 260px 260px, rgba(150,190,80,.4), transparent 70%),
      #f6f9ee;
  }
  .front-disc {
    position: absolute; left: 77px; top: 72px; width: 136px; height: 136px;
    border-radius: 50%; background: radial-gradient(circle at 45% 40%, #9cc24a, #78ad36);
    display: flex; align-items: center; justify-content: center;
    font-family: "Nunito", sans-serif; font-weight: 700; font-size: 24px;
    color: var(--paper); letter-spacing: -0.3px;
  }
  .title {
    position: absolute; font-family: "Playfair Display", Georgia, serif; font-weight: 700;
    color: #5a8f34; text-shadow: 2px 2px 0 #8a8a8a; line-height: 1;
  }
  .front-title { left: 18px; top: 254px; width: 260px; }
  .front-title .line1 { display: block; font-size: 40px; padding-left: 30px; }
  .front-title .line2 { display: block; font-size: 38px; margin-top: 4px; }
  .tagline {
    position: absolute; left: 0; width: 100%; top: 458px; text-align: center;
    font-size: 13.5px; line-height: 19px; color: var(--ink);
  }

  /* Right: lid panel and mark sheet */
  .panel-lid {
    position: absolute; left: 643px; top: 0; width: 316px; height: 468px;
    background: linear-gradient(180deg, #76a141 0%, #92b948 45%, #abc54f 100%);
  }
  .lid-disc {
    position: absolute; left: 28px; top: 174px; width: 260px; height: 260px;
    border-radius: 50%; border: 3px solid var(--paper);
    background:
      radial-gradient(circle at 35% 30%, rgba(170,200,80,.9), transparent 55%),
      radial-gradient(circle at 60% 75%, rgba(110,160,45,.9), transparent 60%),
      #86b23d;
    display: flex; align-items: center; justify-content: center;
    font-family: "Nunito", sans-serif; font-weight: 700; font-size: 44px;
    color: var(--paper); letter-spacing: -0.5px;
  }

  .sheet-title { left: 706px; top: 892px; width: 260px; }
  .sheet-title .line1 { display: block; font-size: 46px; padding-left: 34px; }
  .sheet-title .line2 { display: block; font-size: 44px; margin-top: 4px; }

  .swatches { position: absolute; left: 752px; top: 1043px; display: flex; gap: 6px; }
  .swatch { width: 36px; height: 36px; }
  .swatch.ink { background: var(--ink); }
  .swatch.forest { background: var(--forest); }
  .swatch.moss { background: var(--moss); }
  .swatch.leaf { background: var(--leaf); }
  .swatch.lime { background: var(--lime); }

  .caption {
    position: absolute; right: 58px; top: 1098px;
    font-size: 45px; font-weight: 400; color: var(--ink); letter-spacing: .2px;
  }
</style>
</head>
<body>
<main class="sheet">

  <section class="wrap">
    <div class="panel-info">
      <div class="info-table">
        <div class="cell full origin">Single Origin<br>Herbal Tea etc.</div>
        <div class="cell key">Leaf Base:</div>
        <div class="cell">Lemon Verbena<br>Mint<br>Agastache</div>
        <div class="cell key">Petals:</div>
        <div class="cell"></div>
        <div class="cell key">Batch:</div>
        <div class="cell"></div>
        <div class="cell full address">Fernlow Creek<br>Victoria Australia</div>
      </div>
    </div>

    <div class="panel-brand">
      <div class="brand-disc">verdancy</div>
    </div>

    <div class="panel-front">
      <div class="front-art" role="img" aria-label="Watercolour green wash with line-drawn leaves, flowers and a steaming cup of herbal tea"></div>
      <div class="front-disc">verdancy</div>
      <h1 class="title front-title"><span class="line1">Brook</span><span class="line2">&amp; Thistle</span></h1>
      <p class="tagline">Grown, harvested and dried<br>Chemical free on our farm in east Marrowvale</p>
    </div>
  </section>

  <section class="panel-lid">
    <div class="lid-disc">verdancy</div>
  </section>

  <h2 class="title sheet-title"><span class="line1">Brook</span><span class="line2">&amp; Thistle</span></h2>

  <div class="swatches">
    <span class="swatch ink"></span>
    <span class="swatch forest"></span>
    <span class="swatch moss"></span>
    <span class="swatch leaf"></span>
    <span class="swatch lime"></span>
  </div>

  <p class="caption">Brook and Thistle Label</p>

</main>
</body>
</html>
```